Quick Straightforward Billboard Redesign

- Design billboard sized for 10 foot' x 36' foot width live area size and please include bleeds 6" around all sides
- Exact blue color match is imperative in headline, logo, phone number bubble or wherever used. C-83 / M-45 / Y-1 / K-0-
- What I hope to illustrate is that our company offers the best porch screening in the area area, in regards to quality, expertise, durability, storms proof, but we do not build screen porches.
- Current board is attached below from previous designer, and as you can see sizing was off, white space on edges make it appear to be sized incorrectly.
- I also attached my own little mock up idea well well if it helps, favorite image, logo, headline, etc and ideas perhaps on expanding or making this better?

Thanks so much!

Target Market(s)

Drivers and passengers, Southeastern NC, are of immense new construction and high end homes.

Industry/Entity Type

Construction

Colors
0054AA
0677BA
7BADD7
CADEEF
E8F1F8

Requirements
Must have
• Blue color matching
Nice to have
• Design spins or other thoughts on my little mock up

```html
<!DOCTYPE html>
<html lang="en">
<head>
<meta charset="utf-8">
<title>Tidewater Porchworks Billboard</title>
<link rel="stylesheet" href="https://fonts.googleapis.com/css2?family=Oswald:wght@500;700&family=Montserrat:wght@800&display=swap">
<style>
  :root {
    --brand-blue: #0067b4;
    --deep-blue: #0054aa;
    --brand-green: #00b859;
    --white: #ffffff;
    --stage: #e8f1f8;
    --photo-sky: #9cc6ea;
    --photo-stone: #cfc8bb;
  }
  * { margin: 0; padding: 0; box-sizing: border-box; }
  html, body { width: 1200px; height: 800px; overflow: hidden; }
  body { background: var(--stage); position: relative; }

  .billboard {
    position: absolute;
    left: 20px; top: 239px;
    width: 1160px; height: 322px;
    background: var(--white);
    overflow: hidden;
  }
  .billboard__art { position: absolute; inset: 0; width: 100%; height: 100%; }

  .headline {
    position: absolute;
    left: 40px; top: 6px;
    font-family: "Oswald", sans-serif;
    font-weight: 700;
    font-size: 78px;
    line-height: 86px;
    white-space: nowrap;
  }
  .headline__line--blue { color: var(--brand-blue); display: block; }
  .headline__line--green { color: var(--brand-green); display: block; }

  .brand {
    position: absolute;
    left: 40px; top: 226px;
    display: flex; align-items: center; gap: 16px;
  }
  .brand__square { width: 40px; height: 40px; background: var(--brand-blue); }
  .brand__name {
    font-family: "Oswald", sans-serif;
    font-weight: 700;
    font-size: 52px;
    line-height: 1;
    color: var(--brand-blue);
    white-space: nowrap;
  }

  .phone {
    position: absolute;
    left: 746px; top: 264px;
    height: 58px;
    display: flex; align-items: center; gap: 10px;
    font-family: "Montserrat", sans-serif;
    font-weight: 800;
    font-size: 44px;
    color: var(--white);
    white-space: nowrap;
  }
  .phone__icon { width: 30px; height: 30px; }
</style>
</head>
<body>
  <section class="billboard">
    <svg class="billboard__art" viewBox="0 0 1160 322">
      <defs>
        <linearGradient id="porchTones" x1="0" y1="0" x2="0" y2="1">
          <stop offset="0" stop-color="#eef2f4"/>
          <stop offset="0.3" stop-color="#9cc6ea"/>
          <stop offset="0.55" stop-color="#7aa35c"/>
          <stop offset="0.75" stop-color="#cfc8bb"/>
          <stop offset="1" stop-color="#b8afa2"/>
        </linearGradient>
      </defs>
      <rect class="accent-bar" x="16" y="24" width="6" height="150" fill="#00b859"/>
      <polygon class="porch-photo" role="img" aria-label="Photo of a screened coastal porch with wicker seating overlooking a lake"
               points="800,0 1160,0 1160,262 708,262" fill="url(#porchTones)"/>
      <polyline class="accent-bracket" points="808,58 784,58 666,322" fill="none"
                stroke="#00b859" stroke-width="12"/>
      <polygon class="phone-band" points="722,262 1160,262 1160,322 695,322" fill="#0067b4"/>
    </svg>

    <h1 class="headline">
      <span class="headline__line--blue">Screen Your Porch.</span>
      <span class="headline__line--green">Built for the Coast.</span>
    </h1>

    <div class="brand">
      <span class="brand__square"></span>
      <span class="brand__name">TIDEWATER PORCHWORKS</span>
    </div>

    <div class="phone">
      <svg class="phone__icon" viewBox="0 0 24 24" aria-hidden="true">
        <path fill="#fff" d="M6.6 10.8a15.1 15.1 0 0 0 6.6 6.6l2.2-2.2a1 1 0 0 1 1-.25 11.4 11.4 0 0 0 3.6.57 1 1 0 0 1 1 1V20a1 1 0 0 1-1 1A17 17 0 0 1 3 4a1 1 0 0 1 1-1h3.5a1 1 0 0 1 1 1c0 1.25.2 2.45.57 3.570a1 1 0 0 1-.25 1z"/>
      </svg>
      <span class="phone__number">910.555.0142</span>
    </div>
  </section>
</body>
</html>
```